TIVARELCAP web-presence redisign

We would like to have our existing web-presence redesigned. Have a look at www.tivarel.ch (please use explorer). To the existing 11 pages we would add one more.

```html
<!DOCTYPE html>
<html lang="de">
<head>
<meta charset="utf-8">
<title>Tivarel Zahnarztpraxis</title>
<link href="https://fonts.googleapis.com/css2?family=Open+Sans:ital,wght@0,300;0,400;0,700;1,300;1,400&display=swap" rel="stylesheet">
<style>
  :root {
    --ink: #111111;
    --muted: #7a7a7a;
    --accent: #c8793a;
    --gold: #d9a441;
    --rule: #9a9a9a;
    --white: #ffffff;
    --frame: #dcdcdc;
  }
  * { margin: 0; padding: 0; box-sizing: border-box; }
  html, body { width: 1200px; height: 881px; overflow: hidden; background: var(--white); }
  body { font-family: 'Open Sans', sans-serif; color: var(--ink); position: relative; }
  .abs { position: absolute; }

  .brand { left: 101px; top: 46px; display: flex; align-items: center; gap: 10px; }
  .brand-dot { width: 34px; height: 34px; border-radius: 50%; background: var(--gold); }
  .brand-name { font-size: 22px; font-weight: 400; color: #555555; line-height: 1.1; letter-spacing: 0.5px; }

  .phone { right: 136px; top: 30px; display: flex; align-items: center; gap: 7px; color: var(--accent); font-style: italic; font-weight: 300; font-size: 23px; }
  .phone svg { width: 24px; height: 24px; }

  .main-nav { right: 136px; top: 80px; display: flex; gap: 16px; font-size: 17px; color: var(--muted); }
  .main-nav .active { color: var(--accent); }

  .hero { left: 102px; top: 142px; width: 716px; height: 388px; border-radius: 8px; overflow: hidden;
    background: radial-gradient(circle at 82% 30%, #d8b27a 0%, #9a6a2c 35%, #4a2c10 75%), #6b4318; }
  .hero-person { position: absolute; left: 0; top: 0; width: 450px; height: 100%;
    background: linear-gradient(90deg, #e9d6b4 0%, #d7b98a 55%, rgba(200,160,100,0) 100%); }
  .hero-quote { position: absolute; left: 427px; top: 107px; width: 260px; color: var(--white); font-size: 14.5px; line-height: 22.4px; font-weight: 400; }
  .hero-sign { position: absolute; left: 427px; top: 206px; color: #eee2cc; font-size: 13px; font-style: italic; font-weight: 300; }
  .btn-consult { position: absolute; left: 425px; top: 244px; width: 228px; height: 38px; border-radius: 19px; background: #050505; color: var(--white);
    font-weight: 700; font-size: 16px; letter-spacing: 0.4px; display: flex; align-items: center; justify-content: center; }

  .tile { left: 834px; width: 230px; height: 126px; border-radius: 6px; overflow: hidden; }
  .tile-health { top: 142px; background: linear-gradient(135deg, #7da65a, #c9d7a4 60%, #e9dfd2); }
  .tile-aesthetic { top: 274px; background: linear-gradient(135deg, #f2f4f6, #dfe4ea 50%, #e9d8c8); }
  .tile-solution { top: 406px; background: linear-gradient(135deg, #f5ece6, #e8f1f5 50%, #d8eef2); }
  .tile-label { position: absolute; left: 0; bottom: 0; width: 100%; height: 35px; background: rgba(230,230,230,0.65);
    font-size: 20px; font-weight: 300; text-align: center; line-height: 35px; color: #1a1a1a; }
  .tile-health .tile-label { background: rgba(40,40,40,0.55); color: var(--white); }

  .welcome-title { left: 101px; top: 574px; font-size: 25.5px; font-weight: 400; }
  .rule { height: 0; border-top: 1px dashed var(--rule); }
  .welcome-rule { left: 101px; top: 618px; width: 710px; }
  .welcome-text { left: 101px; top: 633px; width: 710px; font-size: 13.6px; line-height: 15.7px; }
  .btn-more { left: 101px; top: 716px; width: 86px; height: 20px; border-radius: 10px; background: #050505; color: var(--white);
    font-size: 8.5px; font-weight: 700; display: flex; align-items: center; justify-content: center; }

  .ba-title { left: 834px; top: 576px; width: 230px; text-align: center; font-size: 16.5px; }
  .ba-frame { left: 834px; top: 604px; width: 230px; height: 108px; border: 1px solid var(--frame); border-radius: 7px; }
  .ba-photo { position: absolute; top: 10px; width: 102px; height: 87px; background: linear-gradient(135deg, #6b3d2a, #b9805e 55%, #3a2418); }
  .ba-before { left: 12px; }
  .ba-after { left: 115px; }
  .ba-caption { left: 834px; top: 720px; width: 230px; text-align: center; font-size: 12px; }

  .footer-rule { left: 101px; top: 769px; width: 962px; }
  .footer-nav { left: 100px; top: 787px; display: flex; gap: 13px; font-size: 12px; color: var(--muted); }
  .copyright { left: 101px; top: 809px; font-size: 12px; color: var(--muted); }
  .contact { left: 838px; top: 788px; font-size: 12px; line-height: 14.5px; }
</style>
</head>
<body>
  <div class="abs brand">
    <span class="brand-dot"></span>
    <span class="brand-name">Tivarel<br>Zahnarztpraxis</span>
  </div>

  <div class="abs phone">
    <svg viewBox="0 0 24 24" aria-hidden="true">
      <circle cx="12" cy="12" r="12" fill="#c8793a"/>
      <path d="M8.5 6.5c.6-.4 1.3-.2 1.6.4l.9 1.8c.2.5.1 1-.3 1.3l-.8.6c.6 1.4 1.6 2.5 3 3.2l.6-.8c.3-.4.9-.5 1.3-.3l1.8.9c.6.3.8 1 .4 1.6l-.7 1c-.5.6-1.3.9-2 .6-3.2-1.1-5.6-3.5-6.7-6.7-.3-.7 0-1.5.6-2z" fill="#ffffff"/>
    </svg>
    <span>+41 (0)44 000 12 34</span>
  </div>

  <nav class="abs main-nav">
    <span>Home</span><span>Zahnmedizin</span><span class="active">Dentalhygiene</span><span>Before &amp; After</span><span>Team</span><span>Kontakt</span>
  </nav>

  <section class="abs hero">
    <div class="hero-person" role="img" aria-label="Portrait photo of a smiling blonde woman"></div>
    <p class="hero-quote">It is our goal to improve your wellbeing. You will enjoy the beauty of everyday life with healthy teeth and laugh heartily in every situation.</p>
    <p class="hero-sign">Dr. med. Lena Marwick</p>
    <div class="btn-consult">FREE CONSULTATION</div>
  </section>

  <div class="abs tile tile-health" role="img" aria-label="Photo of a woman eating an apple in the grass">
    <div class="tile-label">Gesundheit</div>
  </div>
  <div class="abs tile tile-aesthetic" role="img" aria-label="Photo of a dental model being worked on">
    <div class="tile-label">Ästhetik</div>
  </div>
  <div class="abs tile tile-solution" role="img" aria-label="Photo of a patient at a dental treatment">
    <div class="tile-label">Lösungen</div>
  </div>

  <h1 class="abs welcome-title">Welcome to Tivarel Zahnarztpraxis</h1>
  <div class="abs rule welcome-rule"></div>
  <p class="abs welcome-text">Lorem ipsum dolor sit amet, consectetur adipiscing elit. In fermentum dolor non augue pretium egestas. Donec sem eros, tincidunt at congue ut, posuere sit amet est. Vivamus scelerisque viverra odio sit amet laoreet. Ut nec neque non justo rutrum tempor lobortis eu ante.&nbsp; In fermentum dolor non augue pretium egestas. Donec sem eros, tincidunt at congue ut, posuere sit amet est.</p>
  <div class="abs btn-more">LEARN MORE</div>

  <h2 class="abs ba-title" style="font-weight:400">Before and After</h2>
  <div class="abs ba-frame">
    <div class="ba-photo ba-before" role="img" aria-label="Before photo of a patient's smile"></div>
    <div class="ba-photo ba-after" role="img" aria-label="After photo of a patient's smile"></div>
  </div>
  <p class="abs ba-caption">Click here and See the results</p>

  <div class="abs rule footer-rule"></div>
  <nav class="abs footer-nav">
    <span>Home</span><span>Zahnmedizin</span><span>Dentalhygiene</span><span>Before &amp; After</span><span>Team</span><span>Kontakt</span>
  </nav>
  <p class="abs copyright">All rights reserved © 2014 - Privacy Policy</p>
  <p class="abs contact">Add: Lindenweg 12 CH-8000 Musterstadt<br>Email : info@tivarel.ch</p>
</body>
</html>
```